Bright Meadow Kitchen needs your unleashed creativity for a label!

We need labels for the re-launching of our newly redesigned product. The product comes in a yogurt style cup and there will be a sleeve that goes vertically around the container. On that sleeve we need a design/label. The template for the sleeve is attached, our logo that also has our colors, as well as a mock up of how the sleeve will be positioned around the container.

Our product is gluten free, vegan, soy free, and 12 grams of plant protein. We want our product to appeal to anyone eating healthy. Because it's vegan and gluten free, our label designs in the past have had a little bit more of a vegan/yoga/all natural look to it (which it is!) but we want the packaging to appeal to anyone and everyone. We have our product in gyms, juice bars, college cafes, rock climbing places, cross fit gyms, so I hope that gives you an idea of the variety in our clientele.

We want to convey that even though its super healthy, its also super delicious, very convenient, and a fresh baked alternative to run of the mill protein bars. The name of our company is bright meadow kitchen, and the muffin is called sunrise crumble. We would like to emphasis more the "performance" of natural, and the "power" of the product. We are looking for the balance of "natural" and "power" and "performance".

We had an idea of having one of the sides (probably the back or bottom?) have a little blurb about our story, just a few lines, but I am not married to the idea so if you think it would work in your design give it a go, if not that's great too!

We really look forward to seeing your design please let us know if you have any questions!

Industry/Entity Type

Product

Colors

Designer to choose colors to be used in the design.

Requirements
Must have
• A small area to include a upc/barcode on the bottom on the package

```html
<!DOCTYPE html>
<html lang="en">
<head>
<meta charset="utf-8">
<title>Bright Meadow Kitchen – Blueberry Bloom Sleeve</title>
<link href="https://fonts.googleapis.com/css2?family=Arimo:wght@400;700&family=Dancing+Script:wght@600&family=Cinzel:wght@500&family=Oswald:wght@300;500&display=swap" rel="stylesheet">
<style>
  :root {
    --stage: #e4e4e4;
    --paper: #ffffff;
    --paper-tint: #eef2f5;
    --lime: #d5df3f;
    --lime-deep: #c4d12e;
    --berry: #2f5f9c;
    --berry-dark: #1f3f73;
    --teal: #4d8a8f;
    --leaf: #6f9a4a;
    --ink: #111111;
    --olive: #8a8a3a;
  }
  * { box-sizing: border-box; margin: 0; padding: 0; }
  html, body { width: 1200px; height: 1000px; overflow: hidden; }
  body {
    background: var(--stage);
    display: flex;
    align-items: center;
    justify-content: center;
    font-family: "Arimo", Arial, sans-serif;
  }
  .sleeve {
    position: relative;
    width: 660px;
    height: 920px;
    background: linear-gradient(180deg, var(--paper) 0%, var(--paper-tint) 100%);
    box-shadow: 0 6px 24px rgba(0,0,0,.12);
    overflow: hidden;
  }
  .berry-band {
    position: absolute;
    top: 0; left: 0; right: 0;
    height: 150px;
    background: radial-gradient(circle at 20% 50%, #5b82c4 0 14%, transparent 15%),
                radial-gradient(circle at 75% 40%, #4a6fb0 0 12%, transparent 13%),
                var(--lime);
  }
  .faint-berries {
    position: absolute;
    top: 150px; left: 0; right: 0; bottom: 0;
    background: radial-gradient(ellipse at 50% 30%, rgba(200,212,224,.55), rgba(255,255,255,0) 70%);
  }
  .brand {
    position: absolute;
    top: 70px; left: 50%;
    transform: translateX(-50%);
    width: 220px; height: 150px;
    border-radius: 50% 50% 0 0 / 60% 60% 0 0;
    background: var(--paper);
    display: flex; flex-direction: column;
    align-items: center; justify-content: center;
    gap: 10px;
  }
  .brand-dot {
    width: 34px; height: 34px; border-radius: 50%;
    background: var(--lime-deep);
  }
  .brand-name {
    font-family: "Arimo", Arial, sans-serif;
    font-weight: 700;
    font-size: 17px;
    color: var(--olive);
    text-align: center;
    line-height: 1.15;
  }
  .product-name {
    position: absolute;
    top: 215px; left: 0; right: 0;
    text-align: center;
  }
  .product-name .flavour {
    display: block;
    font-family: "Dancing Script", cursive;
    font-size: 78px;
    line-height: 1;
    color: var(--berry);
  }
  .product-name .line {
    display: block;
    font-family: "Cinzel", serif;
    font-size: 30px;
    letter-spacing: 3px;
    color: var(--teal);
    margin-top: -4px;
  }
  .info {
    position: absolute;
    top: 370px; left: 40px;
    width: 430px;
    color: var(--ink);
  }
  .info h2 {
    font-size: 24px;
    font-weight: 700;
    margin-bottom: 16px;
  }
  .info p {
    font-size: 20px;
    line-height: 1.4;
    text-align: justify;
    hyphens: auto;
  }
  .info section + section { margin-top: 40px; }
  .fine-print {
    position: absolute;
    bottom: 28px; left: 40px;
    width: 420px;
    font-size: 12px;
    line-height: 1.35;
    color: #333;
  }
  .claims {
    position: absolute;
    top: 330px; right: 0; bottom: 0;
    width: 165px;
    background: var(--lime);
    display: flex; flex-direction: column;
    align-items: center;
    padding-top: 0;
  }
  .soy-ribbon {
    width: 120px;
    background: var(--paper);
    text-align: center;
    padding: 18px 0 60px;
    clip-path: polygon(0 0, 100% 0, 100% 100%, 50% 86%, 0 100%);
    color: var(--lime-deep);
    font-family: "Oswald", sans-serif;
  }
  .soy-ribbon .soy { display: block; font-weight: 300; font-size: 54px; line-height: 1; }
  .soy-ribbon .free { display: block; font-weight: 500; font-size: 34px; letter-spacing: 4px; line-height: 1.2; }
  .soybean-art {
    width: 70px; height: 80px; margin: 14px auto 0;
    border-radius: 40%;
    background: var(--lime);
  }
  .gluten-seal {
    margin-top: 40px;
    width: 120px; height: 120px;
    border-radius: 50%;
    border: 6px solid var(--paper);
  }
  .vegan-mark {
    margin-top: 40px;
    width: 120px; height: 60px;
    border-radius: 10px;
    background: linear-gradient(90deg, rgba(255,255,255,.85), rgba(255,255,255,.6));
  }
</style>
</head>
<body>
  <article class="sleeve">
    <div class="berry-band" role="img" aria-label="Watercolour blueberries and leaves on lime green"></div>
    <div class="faint-berries" role="img" aria-label="Faint pale blueberry pattern"></div>

    <div class="brand">
      <span class="brand-dot"></span>
      <span class="brand-name">Bright Meadow<br>Kitchen</span>
    </div>

    <h1 class="product-name">
      <span class="flavour">Blueberry</span>
      <span class="line">BLOOM</span>
    </h1>

    <div class="info">
      <section class="ingredients">
        <h2>INGREDIENTS:</h2>
        <p>Carrot, gluten free flour blend (brown rice, potato starch), apple, hemp seed, oats, raw turbinado, sugar, dried blueberries, vanilla extract (alcohol free), flax seed, chia seed, sea salt, sodium bicarbonate (aluminum free), organic</p>
      </section>
      <section class="nutrition">
        <h2>NUTRITION FACTS:</h2>
        <p>Duis scelerisque, sit venenatis condimentum ipsum bibendum, sociis mauris nibh sapien, mi vulputate lectus a dui ante nunc. Tellus aliquam, pretium urna, ut suspendisse ultricies donec, enim donec fringilla, taciti augue condimentum. Fuga wisi justo, ac volutpat nibh nulla, euismod dolor sit molestie in.</p>
      </section>
    </div>

    <p class="fine-print">Est ante tincidunt nisl, maecenas neque quis elit et nec cras, nulla odio pellentesque vivamus auctor</p>

    <aside class="claims">
      <div class="soy-ribbon">
        <span class="soy">SOY</span>
        <span class="free">FREE</span>
        <div class="soybean-art" role="img" aria-label="Soybean pod icon"></div>
      </div>
      <div class="gluten-seal" role="img" aria-label="Gluten free seal"></div>
      <div class="vegan-mark" role="img" aria-label="Hand lettered vegan mark"></div>
    </aside>
  </article>
</body>
</html>
```